Kerno Solutions: searching for a flyer to trow in letterboxes for properties we are interested in

Hello ,

Introduction:
We are a company based in Luxembourg called "Kerno Solutions". We are specialized in buying properties on which we develop and build constructions before selling them.

Informations for the flyer:
We need a flyer to trow into the letter boxes of property owners letting them know that we are interested in buying their property, if they are interested they can give us a call.

The text for the flyer/letter is in the attachment called >>2020-03-11_KS_Text for flyer,letter there might be slight changes<<.

We need to look competent, professional and financially stable.

The flyer needs to be short and not over welling with information otherwise it will land in the trash.

We have decided that we don't want real pictures on the flyer, but shapes of any kind, blue prints, drawings are fine.

Format should be in DIN A4. We plan to print the flyer on both sides in two different languages, in other words the design will be the same on both sides only the text will be in a different language.

I also added our current logo and here is the design of the website that is under construction at the moment http://www.kernosolutions-example.lu/. The logo's color can be changed into a different blue or uni color (all white or all black).
Updates

Hi, First time user the howl thing started faster as expected. Furthermore, I need to catch my boss to discust the project with him and he is on a lot of meetings. Please give us a little bit more time. Thanks

Target Market(s)

Property owners

Requirements
Must have
• email, phone number, tax number (RCS), Tax number , matriculation and address.
see word file in attachment for information
Nice to have
• Our company logo, in one form or an other, you can be creative, the logo is in the attachment.
Should not have
• Real pictures

```html
<!DOCTYPE html>
<html lang="fr">
<head>
<meta charset="utf-8">
<title>Kerno Solutions – Flyer A4 recto / verso</title>
<link rel="stylesheet" href="https://fonts.googleapis.com/css2?family=Montserrat:wght@400;500&family=Oswald:wght@500&display=swap">
<style>
  :root {
    --blue: #0f5f8f;
    --blue-dark: #0a2b42;
    --blue-soft: #3f86b3;
    --ink: #2e2e2e;
    --band-dark: #262626;
    --canvas: #ffffff;
    --paper: #ffffff;
    --paper-shade: #eef0f2;
    --white: #ffffff;
  }
  * { box-sizing: border-box; margin: 0; padding: 0; }
  html, body {
    width: 1200px; height: 2598px; overflow: hidden;
    background: var(--canvas);
  }
  .sheet-stack {
    position: absolute; left: 176px; top: 66px;
    display: flex; flex-direction: column; gap: 66px;
  }
  .sheet {
    width: 848px; height: 1201px; position: relative; overflow: hidden;
    box-shadow: 0 6px 22px rgba(0,0,0,.28);
    background: var(--paper);
  }
  .sheet-inner {
    position: absolute; left: 0; top: 0;
    width: 538px; height: 762px;
    transform: scale(1.5762); transform-origin: 0 0;
    background:
      linear-gradient(135deg, transparent 55%, rgba(220,224,228,.45) 55%, transparent 78%),
      linear-gradient(200deg, var(--paper) 40%, var(--paper-shade) 100%);
    font-family: "Montserrat", Arial, sans-serif;
  }
  .header-ornament {
    position: absolute; left: 22px; top: 12px; width: 494px; height: 216px;
    border-radius: 10px;
    background: linear-gradient(100deg, var(--blue) 0%, var(--blue-soft) 50%, var(--blue-dark) 100%);
  }
  .brand-name {
    position: absolute; left: 0; top: 150px; width: 538px;
    display: flex; justify-content: center; align-items: center; gap: 7px;
    font-family: "Oswald", "Arial Narrow", sans-serif; font-weight: 500;
    font-size: 27px; color: var(--white); letter-spacing: .2px;
  }
  .brand-mark { width: 12px; height: 12px; background: var(--white); }
  .salutation {
    position: absolute; left: 41px; top: 288px;
    font-size: 14px; color: var(--blue);
  }
  .letter-body {
    position: absolute; left: 42px; top: 348px; width: 458px;
    font-size: 13.6px; line-height: 21.5px; color: var(--ink);
  }
  .letter-body p { margin-bottom: 21.5px; }
  .signature {
    position: absolute; left: 41px; top: 630px;
    font-size: 14px; color: var(--blue);
  }
  .footer { position: absolute; left: 0; top: 700px; width: 538px; height: 62px; }
  .footer-bands { position: absolute; inset: 0; }
  .footer-company {
    position: absolute; left: 41px; top: 12px; color: var(--white);
    font-size: 11.5px; line-height: 18px; white-space: nowrap;
  }
  .footer-contact {
    position: absolute; left: 294px; top: 11px; color: var(--white);
    font-size: 8px; line-height: 13.5px; white-space: nowrap;
  }
  .footer-line { display: flex; align-items: center; gap: 4px; }
  .footer-line svg { flex: none; }
</style>
</head>
<body>
<main class="sheet-stack">

  <!-- Recto : français -->
  <article class="sheet">
    <div class="sheet-inner">
      <div class="header-ornament" role="img" aria-label="Blue folded frame ornament around the company name"></div>
      <div class="brand-name"><span class="brand-mark"></span>Kerno Solutions</div>

      <p class="salutation">Madame, Monsieur,</p>
      <div class="letter-body">
        <p>Ce courrier vous a été adressé, car votre propriété a attiré notre attention. Nous souhaiterions discuter avec vous de son éventuel rachat par notre société.</p>
        <p>En cas d’accord, nous vous assurons une décision rapide, un paiement garanti, et zéro frais d’intermédiaire.</p>
        <p>En attendant de vos nouvelles, nous restons à votre entière disposition pour tout renseignement.</p>
        <p>Salutations distinguées,</p>
      </div>
      <p class="signature">L’équipe de Kerno Solutions</p>

      <footer class="footer">
        <svg class="footer-bands" viewBox="0 0 538 62" aria-hidden="true">
          <rect x="270" y="0" width="268" height="62" fill="#0f5f8f"/>
          <path d="M0 0 H268 Q280 0 280 12 V62 H0 Z" fill="#262626"/>
        </svg>
        <div class="footer-company">
          <div>Company name : Kerno Solutions sàrl</div>
          <div class="footer-line">
            <svg width="11" height="11" viewBox="0 0 24 24"><path fill="#fff" d="M6.6 10.8a15 15 0 0 0 6.6 6.6l2.2-2.2a1 1 0 0 1 1-.25 11.4 11.4 0 0 0 3.6.6 1 1 0 0 1 1 1V20a1 1 0 0 1-1 1A17 17 0 0 1 3 4a1 1 0 0 1 1-1h3.5a1 1 0 0 1 1 1c0 1.25.2 2.45.6 3.6a1 1 0 0 1-.25 1z"/></svg>
            691 000 482
          </div>
        </div>
        <div class="footer-contact">
          <div class="footer-line">
            <svg width="8" height="8" viewBox="0 0 24 24"><path fill="#fff" d="M2 5h20v14H2z M2 5l10 8 10-8" stroke="#0f5f8f" stroke-width="1.5"/></svg>
            info@kernosolutions-example.lu
          </div>
          <div class="footer-line">
            <svg width="8" height="8" viewBox="0 0 24 24"><circle cx="12" cy="12" r="10" fill="none" stroke="#fff" stroke-width="2"/><path d="M2 12h20M12 2c4 4 4 16 0 20M12 2c-4 4-4 16 0 20" fill="none" stroke="#fff" stroke-width="1.6"/></svg>
            www.kernosolutions-example.lu
          </div>
          <div class="footer-line">
            <svg width="8" height="8" viewBox="0 0 24 24"><path fill="#fff" d="M12 3 2 12h3v9h5v-6h4v6h5v-9h3z"/></svg>
            18 rue de l’Exemple, L-3000 Kernange
          </div>
        </div>
      </footer>
    </div>
  </article>

  <!-- Verso : lëtzebuergesch -->
  <article class="sheet">
    <div class="sheet-inner">
      <div class="header-ornament" role="img" aria-label="Blue folded frame ornament around the company name"></div>
      <div class="brand-name"><span class="brand-mark"></span>Kerno Solutions</div>

      <p class="salutation">Madame, Monsieur</p>
      <div class="letter-body">
        <p>Dir kritt dëst Schreiwes well Är Proprietéit eis Opmierksamkeet zeréck behalen huet. Mir géinge gär mat lech iwwert d’Méiglechkeet, datt eise Betrib se opkeeft, diskutéieren.</p>
        <p>Mir versécheren lech e séieren Entscheedungsprozess, garantéieren d’Bezuelung a verrechne keng Drëttkäschten.</p>
        <p>Mir géinge eis freeën, vun lech ze héieren, a sti ganz zu Ärer Verfügung fir zousätzlech Informatiounen.</p>
        <p>Mat beschte Gréiss,</p>
      </div>
      <p class="signature">D’Equipe vun Kerno Solutions</p>

      <footer class="footer">
        <svg class="footer-bands" viewBox="0 0 538 62" aria-hidden="true">
          <rect x="270" y="0" width="268" height="62" fill="#0f5f8f"/>
          <path d="M0 0 H268 Q280 0 280 12 V62 H0 Z" fill="#262626"/>
        </svg>
        <div class="footer-company">
          <div>Company name : Kerno Solutions sàrl</div>
          <div class="footer-line">
            <svg width="11" height="11" viewBox="0 0 24 24"><path fill="#fff" d="M6.6 10.8a15 15 0 0 0 6.6 6.6l2.2-2.2a1 1 0 0 1 1-.25 11.4 11.4 0 0 0 3.6.6 1 1 0 0 1 1 1V20a1 1 0 0 1-1 1A17 17 0 0 1 3 4a1 1 0 0 1 1-1h3.5a1 1 0 0 1 1 1c0 1.25.2 2.45.6 3.6a1 1 0 0 1-.25 1z"/></svg>
            691 000 482
          </div>
        </div>
        <div class="footer-contact">
          <div class="footer-line">
            <svg width="8" height="8" viewBox="0 0 24 24"><path fill="#fff" d="M2 5h20v14H2z M2 5l10 8 10-8" stroke="#0f5f8f" stroke-width="1.5"/></svg>
            info@kernosolutions-example.lu
          </div>
          <div class="footer-line">
            <svg width="8" height="8" viewBox="0 0 24 24"><circle cx="12" cy="12" r="10" fill="none" stroke="#fff" stroke-width="2"/><path d="M2 12h20M12 2c4 4 4 16 0 20M12 2c-4 4-4 16 0 20" fill="none" stroke="#fff" stroke-width="1.6"/></svg>
            www.kernosolutions-example.lu
          </div>
          <div class="footer-line">
            <svg width="8" height="8" viewBox="0 0 24 24"><path fill="#fff" d="M12 3 2 12h3v9h5v-6h4v6h5v-9h3z"/></svg>
            18 rue de l’Exemple, L-3000 Kernange
          </div>
        </div>
      </footer>
    </div>
  </article>

</main>
</body>
</html>
```